Update our business cards to match our awesome new website

Need a new design for company business cards. We have recently revamped our website and would like our business cards to get a refresh too. I've uploaded the company artwork, logo, as well as the Branding Deck to better understand the look & feel of our brand. Please visit the website at hollowbrookestatesmi.com.

Industry/Entity Type

Real Estate

Contact Information for Business Card

must use the colors outlined in the Branding Deck uploaded to the site, or the colors of our logo.

Font styles to use
Other font styles liked:
• Calibri

Requirements
Must have
• Required items: Name, title, company logo, address: 218 Fenwick St. Suite 300, Northville, MI 48173, email address: cole@hollowbrookestatesMI.com, company phone 800-555-0193, cell: 248-555-0162
Nice to have
• a more simple design. not complicated
Should not have
• cartoonish characters, or whimsical writing or artwork, stay within our branding colors

```html
<!DOCTYPE html>
<html lang="en">
<head>
<meta charset="utf-8">
<title>Hollowbrook Estates – Business Card</title>
<link href="https://fonts.googleapis.com/css2?family=Open+Sans:wght@400;600;700&display=swap" rel="stylesheet">
<style>
  :root {
    --brand-green: #77b843;
    --icon-green: #6cb33f;
    --ink: #2b2b2b;
    --paper: #ffffff;
    --backdrop: #ececec;
  }
  * { margin: 0; padding: 0; box-sizing: border-box; }
  html, body { width: 1200px; height: 1059px; overflow: hidden; }
  body {
    background: var(--backdrop);
    font-family: "Open Sans", Calibri, sans-serif;
    color: var(--ink);
    position: relative;
  }
  .card {
    position: absolute;
    left: 255px;
    width: 690px;
    height: 392px;
    border-radius: 20px;
    overflow: hidden;
  }
  .card--front { top: 100px; background: var(--paper); }
  .card--back { top: 537px; background: var(--brand-green); }

  .front__band {
    position: absolute; left: 0; right: 0; bottom: 0;
    height: 13px; background: var(--brand-green);
  }
  .front__company {
    position: absolute; left: 44px; top: 208px; width: 272px;
    text-align: right; color: var(--ink); font-weight: 600;
  }
  .front__company-name {
    font-size: 22px; letter-spacing: 0.2px; line-height: 1;
    text-transform: uppercase; display: block; text-align: left;
  }
  .front__company-sub { font-size: 8px; display: block; margin-top: 4px; }

  .front__divider {
    position: absolute; left: 344px; top: 112px;
    width: 2px; height: 168px; background: var(--brand-green);
  }
  .contact { position: absolute; left: 369px; top: 104px; }
  .contact__name {
    font-size: 24px; font-weight: 700; color: var(--brand-green);
    line-height: 1.1; letter-spacing: 0.2px;
  }
  .contact__title { font-size: 17px; line-height: 1.3; margin-bottom: 8px; }
  .contact__list { list-style: none; }
  .contact__item {
    display: flex; align-items: flex-start;
    font-size: 14.5px; line-height: 20px;
  }
  .contact__icon { width: 13px; height: 13px; margin: 4px 5px 0 0; flex: none; fill: var(--icon-green); }
  .contact__link { color: var(--icon-green); }

  .back__company {
    position: absolute; left: 0; right: 0; top: 218px;
    text-align: center; color: var(--paper); font-weight: 400;
  }
  .back__company-name {
    display: block; font-size: 44px; line-height: 1;
    text-transform: uppercase; letter-spacing: 0.5px;
  }
  .back__company-sub {
    display: block; font-size: 15px; text-align: right;
    width: 485px; margin: 6px auto 0;
  }
</style>
</head>
<body>

<section class="card card--front">
  <div class="front__company">
    <span class="front__company-name">Hollowbrook Estates</span>
    <span class="front__company-sub">of Michigan, LLC</span>
  </div>

  <div class="front__divider"></div>

  <div class="contact">
    <h1 class="contact__name">DALTON REYES</h1>
    <p class="contact__title">Owner</p>
    <ul class="contact__list">
      <li class="contact__item">
        <svg class="contact__icon" viewBox="0 0 16 16"><path d="M3.5 1l3 3-2 2c1 2.2 2.8 4 5 5l2-2 3 3-2 2.5C6.5 14.5 1.5 9.5 1 3.5z"/></svg>
        800-555-0193
      </li>
      <li class="contact__item">
        <svg class="contact__icon" viewBox="0 0 16 16"><path d="M1 6c0-2 3-3 7-3s7 1 7 3v1h-3V5.5H4V7H1zM3 8h10l1 6H2z"/></svg>
        248-555-0162
      </li>
      <li class="contact__item">
        <svg class="contact__icon" viewBox="0 0 16 16"><path d="M1 3h14v10H1zM2.5 4.5L8 9l5.5-4.5v-.3H2.5z"/></svg>
        cole@hollowbrookestatesMI.com
      </li>
      <li class="contact__item">
        <svg class="contact__icon" viewBox="0 0 16 16"><circle cx="8" cy="8" r="7"/></svg>
        <span>www.<span class="contact__link">hollowbrookestatesmi</span>.com</span>
      </li>
      <li class="contact__item">
        <svg class="contact__icon" viewBox="0 0 16 16"><path d="M8 0a5.5 5.5 0 0 1 5.5 5.5C13.5 10 8 16 8 16S2.5 10 2.5 5.5A5.5 5.5 0 0 1 8 0zm0 3a2.5 2.5 0 1 0 0 5 2.5 2.5 0 0 0 0-5z"/></svg>
        <span>218 Fenwick St. Suite 300 Northville,<br>MI 48173</span>
      </li>
    </ul>
  </div>

  <div class="front__band"></div>
</section>

<section class="card card--back">
  <div class="back__company">
    <span class="back__company-name">Hollowbrook Estates</span>
    <span class="back__company-sub">of Michigan, LLC</span>
  </div>
</section>

</body>
</html>
```